Thriving Mexican import business needs a new business card

Need a refresher of our current business card. Looking for a lighter background with the logo on one side. We will want this file to be adjustable so we can change names, emails and mobile numbers.
We are open to ideas but maintaining a professional image is critical.
Thankyou,

Target Market(s)

Anyone in food industry

Industry/Entity Type

Wholesale

Contact Information for Business Card

Mark Vellanoweth
Director
Corvan Products & Liquor Pty Ltd
5B Larkfield Ct, Brimsworth VIC 3051
0491325067 (03) 95147286
mark@corvanimports.com.au
corvanimportedgoodsandspirits.com.au

Font styles to use
Serif
Other font styles liked:
• NeoGram Heavy

Requirements
Must have
• Professional yet memorable
Corvan logo
Nice to have
• Chilli or tequila/mexican food pictures
Should not have
• Dark background

```html
<!DOCTYPE html>
<html lang="en">
<head>
<meta charset="utf-8">
<title>Corvan Products &amp; Liquor – Business Card</title>
<link rel="stylesheet" href="https://fonts.googleapis.com/css2?family=Oswald:wght@600&family=Mulish:wght@400;700&display=swap">
<style>
  :root {
    --page: #ece7de;
    --card: #fbecc7;
    --ink: #1d1a17;
    --ink-soft: #57514a;
    --frame: #1d1a17;
    --chilli: #c8261c;
    --chilli-warm: #e9702a;
  }
  * { box-sizing: border-box; margin: 0; padding: 0; }
  html, body { width: 1200px; height: 586px; overflow: hidden; }
  body {
    background: var(--page);
    position: relative;
    font-family: "Mulish", sans-serif;
    color: var(--ink);
  }
  .card {
    position: absolute;
    top: 146px;
    height: 278px;
    background: var(--card);
    box-shadow: 0 2px 6px rgba(0,0,0,.12);
  }
  .card--front { left: 100px; width: 490px; }
  .card--back { left: 614px; width: 477px; }

  .brand-name {
    position: absolute;
    left: 38px;
    top: 26px;
    font-family: "Oswald", sans-serif;
    font-weight: 600;
    font-size: 62px;
    line-height: 1;
    letter-spacing: 1px;
    color: var(--ink);
    text-transform: uppercase;
  }

  .company { position: absolute; left: 38px; top: 164px; }
  .company__name { font-weight: 700; font-size: 11px; line-height: 14px; }
  .company__address { font-size: 11px; line-height: 14px; color: var(--ink-soft); }

  .contact-list { position: absolute; left: 38px; top: 201px; list-style: none; }
  .contact-list li {
    display: flex; align-items: center; gap: 7px;
    font-size: 11px; line-height: 16px; color: var(--ink-soft);
  }
  .contact-list svg { width: 9px; height: 9px; fill: var(--ink); flex: none; }

  .person { position: absolute; right: 28px; top: 200px; text-align: right; }
  .person__name { font-weight: 700; font-size: 14px; letter-spacing: .3px; text-transform: uppercase; }
  .person__role { font-size: 10px; letter-spacing: .5px; color: var(--ink-soft); text-transform: uppercase; margin-top: 2px; }

  .back-frame {
    position: absolute; inset: 9px 9px 10px 10px;
    border: 1px solid var(--frame);
  }
  .back-artwork {
    position: absolute; left: 90px; top: 50px; width: 302px; height: 160px;
    background: radial-gradient(ellipse at 55% 40%, var(--chilli) 0%, var(--chilli-warm) 45%, rgba(233,112,42,.25) 75%, transparent 100%);
    border-radius: 40px;
  }
  .website {
    position: absolute; left: 0; right: 0; top: 236px;
    text-align: center; font-weight: 700; font-size: 10.5px; letter-spacing: .2px;
  }
</style>
</head>
<body>
  <section class="card card--front">
    <h1 class="brand-name">Corvan</h1>

    <div class="company">
      <p class="company__name">Corvan Products &amp; Liquor Pty Ltd</p>
      <p class="company__address">5B Larkfield Ct, Brimsworth VIC 3051</p>
    </div>

    <ul class="contact-list">
      <li>
        <svg viewBox="0 0 10 10" aria-hidden="true"><path d="M2 0.5 3.6 2.6 2.7 3.7C3.3 5 4.9 6.6 6.3 7.3L7.4 6.4 9.5 8 8.5 9.5C4.5 9.5 0.5 5.5 0.5 1.5Z"/></svg>
        0491325067
      </li>
      <li>
        <svg viewBox="0 0 10 10" aria-hidden="true"><path d="M2.5 0h5a1 1 0 0 1 1 1v8a1 1 0 0 1-1 1h-5a1 1 0 0 1-1-1V1a1 1 0 0 1 1-1Zm.5 1.2v6.6h4V1.2Z"/></svg>
        (03) 95147286
      </li>
      <li>
        <svg viewBox="0 0 10 10" aria-hidden="true"><path d="M0 2h10v6H0Zm1 .8 4 2.8 4-2.8Z"/></svg>
        mark@corvanimports.com.au
      </li>
    </ul>

    <div class="person">
      <p class="person__name">Mark Vellanoweth</p>
      <p class="person__role">Director</p>
    </div>
  </section>

  <section class="card card--back">
    <div class="back-frame"></div>
    <div class="back-artwork" role="img" aria-label="Illustration of red chillies and sliced chilli rings framed by black and orange Mexican folk-art flourishes and a food and liquor banner"></div>
    <p class="website">www.corvanimportedgoodsandspirits.com.au</p>
  </section>
</body>
</html>
```